Chic streamline modern edgy! Danemerecurls.com

I need a website built for my personal business. I am a hair stylist and I would like a crisp website that works well, is sleek, easy to use, and allows my clients to navigate through Services and pay deposits for services listed.

My logo is somewhat of a full moon, so my theme is nocturnal.

My information can be found at chairbook.com/danemerecurls

Target Market(s)

Women ages 25-55 who are looking for luxury hair extension services

Industry/Entity Type

Hair And Beauty

Number of Pages Required

1 page

Colors
474747
919191
d3d3d3
000000

Requirements
Must have
• Location map, coinvale link embedded for deposits, contact box, bio, faq/policies, menu of services, hours of availability by appointment only .
Nice to have
• An interactive calander where I could post dates that I am available, preferred providers for other beauty services where i could list other websites for make up and other beauty related referrals. a bridal tab would be nice to offer information about bridal services and policies.

```html
<!DOCTYPE html>
<html lang="en">
<head>
<meta charset="utf-8">
<title>Danemere Curls — Hair Studio</title>
<link rel="stylesheet" href="https://fonts.googleapis.com/css2?family=Roboto:ital,wght@0,300;0,400;0,500;0,700;1,400&display=swap">
<style>
:root{
  --black:#000000;
  --charcoal:#474747;
  --slate:#3d3d3d;
  --mid:#919191;
  --light:#d3d3d3;
  --white:#ffffff;
  --deep:#1a1a1a;
  --footer:#262626;
}
*{margin:0;padding:0;box-sizing:border-box}
html,body{width:1200px;height:5172px;overflow:hidden;background:var(--charcoal)}
body{font-family:"Roboto",Arial,sans-serif;color:var(--light);position:relative}
.page{position:relative;width:1200px;height:5172px;overflow:hidden}
section,header,nav,footer{position:absolute;left:0;width:1200px}
.abs{position:absolute}
.section-title{position:absolute;left:0;width:1200px;text-align:center;font-weight:400;font-size:50px;letter-spacing:1px;color:var(--black);text-transform:uppercase}
.section-title.light{color:var(--mid)}
.title-rule{position:absolute;left:450px;width:300px;height:1px;background:linear-gradient(90deg,transparent,rgba(255,255,255,.35),transparent)}

/* buttons */
.pill{position:absolute;display:flex;align-items:center;border-radius:40px;background:linear-gradient(180deg,#e6e6e6,#9a9a9a 55%,#6e6e6e);color:var(--white);font-size:24px;letter-spacing:1px;text-transform:uppercase;box-shadow:0 3px 8px rgba(0,0,0,.5)}
.pill .dot{width:42px;height:42px;border-radius:50%;background:#2a2a2a;border:2px solid #555;display:flex;align-items:center;justify-content:center;margin:0 14px 0 6px}
.pill.dark{background:#2e2e2e;color:var(--mid);font-size:22px;box-shadow:none;border:1px solid #555}
.pill.dark .dot{width:36px;height:36px;background:#555;border:none;margin-left:8px}

/* hero */
.hero{top:0;height:586px;background:var(--black)}
.hero-photo{position:absolute;left:430px;top:0;width:770px;height:586px;background:radial-gradient(ellipse at 65% 45%,#5a5a5a 0%,#2c2c2c 40%,#0c0c0c 75%)}
.brand-mark{position:absolute;left:76px;top:90px;width:110px;height:110px;border-radius:50%;background:var(--white);display:flex;align-items:center;justify-content:center;color:var(--black);font-size:16px;font-weight:500;letter-spacing:1px;text-align:center;line-height:1.2}
.hero-heading{position:absolute;left:86px;top:330px;font-weight:300;font-size:38px;line-height:50px;color:var(--mid)}

/* nav */
.topbar{top:586px;height:90px;background:linear-gradient(180deg,#f2f2f2,#bdbdbd);border-bottom:3px solid #333}
.nav-brand{position:absolute;left:86px;top:14px;display:flex;align-items:center;gap:14px;color:#3a3a3a;font-size:22px;font-weight:500;letter-spacing:3px}
.nav-brand .disc{width:62px;height:62px;border-radius:50%;background:#1d1d1d}
.menu{position:absolute;left:478px;top:22px;height:46px;display:flex;align-items:center;list-style:none;font-size:17px;color:#333;text-transform:uppercase}
.menu li{padding:0 14px;border-left:1px solid #555;line-height:22px}
.menu li:first-child{border-left:none}
.menu li.active{background:var(--black);color:var(--white);line-height:46px;padding:0 18px;margin-right:6px}

/* services */
.services{top:676px;height:669px;background:var(--charcoal)}
.services .intro{position:absolute;left:330px;top:160px;width:540px;text-align:center;font-size:20px;line-height:32px;color:var(--black)}
.svc{position:absolute;top:224px;width:316px;height:316px;border-radius:50%;background:#2a2a2a;border:6px solid #1a1a1a;box-shadow:0 0 0 2px #555;text-align:center;color:var(--white)}
.svc.featured{background:var(--black)}
.svc svg{position:absolute;left:118px;top:34px}
.svc h3{position:absolute;left:0;width:100%;top:126px;font-size:30px;font-weight:500}
.svc p{position:absolute;left:40px;width:224px;top:172px;font-size:14px;line-height:18px;color:var(--light)}
.svc .price{position:absolute;left:0;width:100%;top:246px;font-size:34px;font-weight:700}
.pager{position:absolute;top:608px;left:0;width:1200px;display:flex;justify-content:center;gap:12px}
.pager i{width:12px;height:12px;border-radius:50%;background:#333}
.pager i.on{background:#111}

/* about */
.about{top:1345px;height:679px;background:var(--black)}
.about-photo{position:absolute;left:69px;top:165px;width:517px;height:514px;background:radial-gradient(ellipse at 50% 45%,#6a6a6a 0%,#3a3a3a 40%,#000 78%)}
.bio{position:absolute;left:614px;top:148px;width:510px;font-size:14px;line-height:27px;color:#8a8a8a;text-align:justify}
.read-more{position:absolute;left:614px;top:455px;font-size:14px;color:#bbb}

/* availability */
.availability{top:2024px;height:666px;background:var(--charcoal)}
.calendar{position:absolute;left:86px;top:183px;width:507px;border:2px solid #5e5e5e;background:#2b2b2b}
.cal-head{height:48px;background:linear-gradient(180deg,#8c8c8c,#6c6c6c);color:var(--black);font-size:22px;font-weight:500;text-align:center;line-height:48px;text-transform:uppercase}
.calendar table{width:100%;border-collapse:collapse;table-layout:fixed}
.calendar th{height:36px;background:#1c1c1c;color:var(--light);font-size:14px;font-weight:500;border:1px solid #444}
.calendar td{height:56px;border:1px solid #444;font-size:13px;color:#9a9a9a;text-align:center}
.calendar td.booked{background:#161616;box-shadow:inset 0 0 0 2px #555}
.hours{position:absolute;left:614px;top:183px;width:500px;height:276px;border:2px solid #5e5e5e;background:#2b2b2b}
.hours .cal-head{font-size:22px}
.hours dl{position:absolute;left:100px;top:72px;width:330px;font-size:16px;color:var(--white);display:grid;grid-template-columns:130px 40px 1fr;row-gap:13px}
.hours dt{font-weight:700}

/* testimonials */
.testimonials{top:2690px;height:672px;background:var(--black)}
.testi-photo{position:absolute;left:300px;top:90px;width:600px;height:582px;background:radial-gradient(ellipse at 50% 40%,#3c3c3c 0%,#1a1a1a 45%,#000 75%)}
.avatar{position:absolute;left:517px;top:155px;width:172px;height:172px;border-radius:50%;background:radial-gradient(circle at 50% 40%,#7a7a7a,#3a3a3a);border:6px solid #666}
.quote-mark{position:absolute;top:320px;font-size:120px;font-weight:700;color:#4d4d4d;line-height:1}
blockquote{position:absolute;left:260px;top:275px;width:680px;text-align:center;font-style:italic;font-size:20px;line-height:34px;color:var(--white)}
.cite{position:absolute;left:0;width:1200px;top:482px;text-align:center;font-size:34px;font-weight:700;color:var(--white)}
.cite-date{position:absolute;left:0;width:1200px;top:532px;text-align:center;font-size:14px;color:#aaa}
.arrows{position:absolute;left:0;width:1200px;display:flex;justify-content:center;gap:14px}
.arrows span{width:36px;height:36px;border-radius:50%;background:#555;display:flex;align-items:center;justify-content:center}
.arrows span.on{background:#ccc}

/* gallery */
.gallery{top:3362px;height:800px;background:var(--charcoal)}
.look{position:absolute;width:228px;height:228px;border-radius:50%;border:8px solid #8a8a8a;box-shadow:0 4px 10px rgba(0,0,0,.5)}

/* map */
.location-map{top:4162px;height:355px;background:linear-gradient(135deg,#e6e6e6,#cfcfcf)}

/* contact */
.contact{top:4517px;height:569px;background:var(--charcoal)}
.field{position:absolute;left:86px;width:500px;height:48px;border-radius:24px;background:#353535;border:1px solid #2a2a2a;padding-left:26px;line-height:46px;font-size:14px;color:#9a9a9a;box-shadow:inset 0 2px 5px rgba(0,0,0,.5)}
.field.message{left:614px;width:500px;height:217px;top:155px;border-radius:18px;line-height:normal;padding-top:16px}

/* footer */
.site-footer{top:5086px;height:86px;background:var(--footer)}
.copyright{position:absolute;left:86px;top:34px;font-size:12px;color:#777}
.pay-name{position:absolute;left:520px;top:24px;font-size:32px;font-weight:700;color:#4d4d4d}
.socials{position:absolute;left:842px;top:26px;display:flex;gap:10px}
.socials i{width:36px;height:36px;border-radius:50%;background:#555}
.book-name{position:absolute;left:990px;top:30px;font-size:22px;font-weight:500;color:#555}
</style>
</head>
<body>
<div class="page">

<header class="hero">
  <div class="hero-photo" role="img" aria-label="Black and white profile portrait of a woman with sleek styled hair"></div>
  <div class="brand-mark">DANEMERE<br>CURLS</div>
  <h1 class="hero-heading">Beautiful Hair is<br>Every Woman's<br>Perfect Ornament!</h1>
  <a class="pill dark" style="left:86px;top:480px;width:218px;height:54px">
    <span class="dot"><svg width="16" height="16" viewBox="0 0 16 16"><path d="M4 2l7 6-7 6" fill="none" stroke="#fff" stroke-width="2.5"/></svg></span>Book Now</a>
</header>

<nav class="topbar">
  <div class="nav-brand"><span class="disc"></span>DANEMERE CURLS</div>
  <ul class="menu">
    <li class="active">Home</li><li>Meet Dane</li><li>Services</li><li>Gallery</li><li>Testimonials</li><li>Contact</li>
  </ul>
</nav>

<section class="services">
  <h2 class="section-title" style="top:40px">Services</h2>
  <div class="title-rule" style="top:108px"></div>
  <p class="intro">Lorem ipsum dolor sit amet, consectetur adipiscing elit. Phasellus non massa vel eros congue dapibus at a leo.</p>

  <article class="svc" style="left:90px">
    <svg width="80" height="80" viewBox="0 0 80 80"><g fill="none" stroke="#fff" stroke-width="5"><circle cx="18" cy="58" r="10"/><circle cx="62" cy="58" r="10"/><path d="M25 50L62 10M55 50L18 10"/></g></svg>
    <h3>Extension removal</h3>
    <p>Removing sewn in extensions, wash, Deep condition, blow dry, trim, and natural hair assessment are...</p>
    <div class="price">$75</div>
  </article>
  <article class="svc featured" style="left:445px">
    <svg width="80" height="80" viewBox="0 0 80 80"><g fill="#fff"><path d="M50 8l22 22-8 8-22-22z"/><path d="M44 24l12 12-30 30-10 2 2-10z" fill="none" stroke="#fff" stroke-width="5"/></g></svg>
    <h3>Color services</h3>
    <p>In person consultation required for new clients Single process color involves the application of permanent...</p>
    <div class="price">$125</div>
  </article>
  <article class="svc" style="left:800px">
    <svg width="80" height="80" viewBox="0 0 80 80"><circle cx="40" cy="40" r="38" fill="#fff"/><circle cx="40" cy="30" r="12" fill="#2a2a2a"/><path d="M18 64c4-14 40-14 44 0z" fill="#2a2a2a"/></svg>
    <h3>Consultation</h3>
    <p>Hair consultations can be crucial and necessary for new Clients. This is a perfect way for me to gauge...</p>
    <div class="price">$55</div>
  </article>
  <div class="pager"><i></i><i class="on"></i><i></i><i></i></div>
</section>

<section class="about">
  <h2 class="section-title light" style="top:44px">Meet Dane Mere</h2>
  <div class="title-rule" style="top:112px"></div>
  <div class="about-photo" role="img" aria-label="Portrait of the stylist in a camouflage jacket"></div>
  <p class="bio">Professional hair stylist Dane Mere has developed a signature approach to hair design. Dane studied the science of beautiful hair at Rowan Academy and continues to sharpen his skill set with continued color and cutting education from leading salon educators. His passion for healthy hair care is reflected in flawless, undetectable extensions. These additions not only accentuate his clients' appearance, they promote growth and protection of their natural mane. To further his artistic technique, Dane travels to hair shows and events in the states and abroad.</p>
  <a class="read-more">» Read More</a>
  <a class="pill" style="left:614px;top:572px;width:220px;height:50px;font-size:20px">
    <span class="dot" style="width:36px;height:36px"><svg width="14" height="14" viewBox="0 0 16 16"><path d="M4 2l7 6-7 6" fill="none" stroke="#fff" stroke-width="2.5"/></svg></span>Book Now</a>
</section>

<section class="availability">
  <h2 class="section-title" style="top:44px">Availability</h2>
  <div class="title-rule" style="top:112px"></div>
  <div class="calendar">
    <div class="cal-head">March 2016</div>
    <table>
      <tr><th>MON</th><th>TUE</th><th>WED</th><th>THU</th><th>FRI</th><th>SAT</th><th>SUN</th></tr>
      <tr><td></td><td>1</td><td>2</td><td>3</td><td>4</td><td>5</td><td>6</td></tr>
      <tr><td>7</td><td>8</td><td>9</td><td>10</td><td>11</td><td>12</td><td>13</td></tr>
      <tr><td>14</td><td>15</td><td>16</td><td>17</td><td>18</td><td>19</td><td>20</td></tr>
      <tr><td>21</td><td>22</td><td>23</td><td>24</td><td>25</td><td class="booked">26</td><td>27</td></tr>
      <tr><td>28</td><td>29</td><td>30</td><td>31</td><td></td><td></td><td></td></tr>
    </table>
  </div>
  <div class="hours">
    <div class="cal-head">Business Hours</div>
    <dl>
      <dt>Tuesday</dt><dd>:</dd><dd>7:00am - 7:00pm</dd>
      <dt>Wednesday</dt><dd>:</dd><dd>7:00am - 7:00pm</dd>
      <dt>Thursday</dt><dd>:</dd><dd>7:00am - 7:00pm</dd>
      <dt>Friday</dt><dd>:</dd><dd>7:00am - 7:00pm</dd>
      <dt>Saturday</dt><dd>:</dd><dd>7:00am - 7:00pm</dd>
    </dl>
  </div>
  <a class="pill" style="left:614px;top:483px;width:500px;height:78px;font-size:32px">
    <span class="dot" style="width:62px;height:62px;background:#1d2f5e;border-color:#3a5aa8"><svg width="22" height="22" viewBox="0 0 16 16"><path d="M4 2l7 6-7 6" fill="none" stroke="#fff" stroke-width="2.5"/></svg></span>Book an Appointment</a>
</section>

<section class="testimonials">
  <div class="testi-photo" role="img" aria-label="Back view of a woman with a glossy dark bob haircut"></div>
  <h2 class="section-title light" style="top:44px">Testimonials</h2>
  <div class="title-rule" style="top:112px"></div>
  <div class="avatar" role="img" aria-label="Client portrait"></div>
  <div class="quote-mark" style="left:80px">“</div>
  <div class="quote-mark" style="left:1040px">”</div>
  <blockquote>"He works with passion. You can actually see it in his eyes you're in his chair. He cares about the health of your hair as well as the look. You can't beat quality service like his. You just can't! I look and feel FABULOUS!!!!!"</blockquote>
  <div class="cite">Carla M.</div>
  <div class="cite-date">12th August, 2015</div>
  <div class="arrows" style="top:592px">
    <span><svg width="12" height="12" viewBox="0 0 16 16"><path d="M11 2L4 8l7 6" fill="none" stroke="#222" stroke-width="3"/></svg></span>
    <span class="on"><svg width="12" height="12" viewBox="0 0 16 16"><path d="M5 2l7 6-7 6" fill="none" stroke="#222" stroke-width="3"/></svg></span>
  </div>
</section>

<section class="gallery">
  <h2 class="section-title" style="top:44px">Gallery</h2>
  <div class="title-rule" style="top:112px"></div>
  <div class="look" style="left:83px;top:172px;background:radial-gradient(circle,#9a9a9a,#4a4a4a)" role="img" aria-label="Client with long curly hair"></div>
  <div class="look" style="left:363px;top:172px;background:radial-gradient(circle,#c7a073,#6a4a2a)" role="img" aria-label="Client with long blonde waves"></div>
  <div class="look" style="left:621px;top:172px;background:radial-gradient(circle,#8a8a8a,#2f2f2f)" role="img" aria-label="Client with voluminous styled hair"></div>
  <div class="look" style="left:879px;top:172px;background:radial-gradient(circle,#7a7a7a,#222)" role="img" aria-label="Client with long sleek hair"></div>
  <div class="look" style="left:83px;top:437px;background:radial-gradient(circle,#7a7a7a,#2a2a2a)" role="img" aria-label="Client with a short tapered cut"></div>
  <div class="look" style="left:363px;top:437px;background:radial-gradient(circle,#a0a0a0,#3a3a3a)" role="img" aria-label="Client with a straight bob"></div>
  <div class="look" style="left:621px;top:437px;background:radial-gradient(circle,#909090,#2a2a2a)" role="img" aria-label="Client with shoulder-length layers"></div>
  <div class="look" style="left:879px;top:437px;background:radial-gradient(circle,#6a6a6a,#1a1a1a)" role="img" aria-label="Client with a sleek asymmetrical cut"></div>
  <div class="arrows" style="top:723px">
    <span><svg width="12" height="12" viewBox="0 0 16 16"><path d="M11 2L4 8l7 6" fill="none" stroke="#222" stroke-width="3"/></svg></span>
    <span class="on"><svg width="12" height="12" viewBox="0 0 16 16"><path d="M5 2l7 6-7 6" fill="none" stroke="#222" stroke-width="3"/></svg></span>
  </div>
</section>

<section class="location-map" role="img" aria-label="Street map showing the salon location"></section>

<section class="contact">
  <h2 class="section-title" style="top:44px">Contact Us</h2>
  <div class="title-rule" style="top:112px"></div>
  <div class="field" style="top:155px">Your Name:</div>
  <div class="field" style="top:235px">Your Phone Number:</div>
  <div class="field" style="top:314px">Your Email:</div>
  <div class="field message">Your Message:</div>
  <a class="pill" style="left:465px;top:421px;width:266px;height:79px;font-size:30px">
    <span class="dot" style="width:56px;height:56px"><svg width="20" height="20" viewBox="0 0 16 16"><path d="M4 2l7 6-7 6" fill="none" stroke="#fff" stroke-width="2.5"/></svg></span>Submit</a>
</section>

<footer class="site-footer">
  <p class="copyright">© 2015 Danemere Curls. All Rights Reserved.</p>
  <span class="pay-name">Coinvale</span>
  <div class="socials" aria-label="Social links"><i></i><i></i><i></i></div>
  <span class="book-name">Chairbook</span>
</footer>

</div>
</body>
</html>
```